RAIL RIGHT FITTERS

We deliver and install grab bars aka grab rails, bath rails, safety rails. same day delivery and installation on almost ANY surface.
not covered by health insurance. most people cannot find anyone to install grab bars. we offer standard grab bars including delivery and installation for $89.95. standard includes choice of white, chrome or pewter 16 inch bars. if 2 bars are installed $84.95 each and 3 for $79.95 each.we also offer designer bars as well as angle configurations.

grab bars can be installed in any room, bathroom, bedroom, kitchen, stairway, garage, workshop, front and backdoor, bathtub, shower stall, toilet area , laundry room and just about any other place you can think of. not only elderly-everyone can benefit                                

Industry/Entity Type

Safety

Requirements
Must have
• eliminate any correlation to brightpath in house website. this flyer should be its own for rail right fitters inc.
Nice to have
• maybe sketch or cartoon in nature ie moving van(delivery)
grab bar attached to van ( product)
character holding on to bar with wrench in other hand (installation)
pricing bursts or clouds enphasizing special $$$

```html
<!DOCTYPE html>
<html lang="en">
<head>
<meta charset="utf-8">
<title>Rail Right Fitters Inc. – Flyer</title>
<link href="https://fonts.googleapis.com/css2?family=Marcellus&family=Marcellus+SC&family=Caladea:wght@400;700&display=swap" rel="stylesheet">
<style>
  :root {
    --ink: #111111;
    --gold: #e5a12a;
    --paper: #ffffff;
    --art-fill: #ececec;
    --sky-top: #8fc4f0;
    --cloud: #eef6fd;
    --grass: #d6eba8;
  }
  html, body {
    margin: 0;
    padding: 0;
    overflow: hidden;
    background: var(--paper);
  }
  .flyer {
    position: relative;
    width: 927px;
    height: 1200px;
    overflow: hidden;
    background: var(--paper);
    color: var(--ink);
    font-family: "Marcellus", serif;
  }
  .flyer p { margin: 0; position: absolute; white-space: nowrap; }

  .bar-art {
    position: absolute;
    background: var(--art-fill);
  }
  .bar-art--left { left: 44px; top: 26px; width: 148px; height: 126px; }
  .bar-art--right { left: 736px; top: 22px; width: 128px; height: 142px; }

  .brand-top {
    left: 0; right: 0; top: 18px;
    text-align: center;
    font-size: 92px;
    color: var(--gold);
  }
  .brand-bottom {
    left: 0; right: 0; top: 132px;
    text-align: center;
    font-size: 100px;
  }
  .tagline {
    left: 0; right: 0; top: 264px;
    text-align: center;
    font-family: "Marcellus SC", serif;
    font-size: 36px;
    letter-spacing: 3px;
    -webkit-text-stroke: 0.8px var(--ink);
  }
  .price { font-size: 38px; }
  .price strong {
    color: var(--gold);
    font-weight: 400;
    -webkit-text-stroke: 0.8px var(--gold);
  }
  .price--single { left: 204px; top: 340px; }
  .price--double { left: 44px; top: 398px; font-size: 37px; }
  .price--triple { left: 592px; top: 398px; font-size: 37px; }
  .finishes {
    left: 50px; top: 448px;
    font-family: "Caladea", serif;
    font-weight: 700;
    font-size: 34px;
  }
  .extras {
    left: 42px; top: 530px;
    font-size: 26px;
    line-height: 42px;
  }

  .scene {
    position: absolute;
    left: 0; top: 622px;
    width: 362px; height: 543px;
    background: linear-gradient(180deg, var(--sky-top) 0%, var(--cloud) 35%, var(--cloud) 80%, var(--grass) 100%);
  }
  .scene__text {
    position: absolute;
    left: 0; width: 350px; top: 82px;
    text-align: center;
    font-size: 46px;
    line-height: 62px;
  }

  .rooms {
    position: absolute;
    left: 450px; width: 400px; top: 556px;
    text-align: center;
    font-family: "Caladea", serif;
    font-size: 34px;
    line-height: 42.5px;
    letter-spacing: 0.5px;
  }
  .rooms__title { font-size: 33px; }
</style>
</head>
<body>
<main class="flyer">
  <div class="bar-art bar-art--left" role="img" aria-label="Illustration of a chrome grab bar mounted diagonally"></div>
  <div class="bar-art bar-art--right" role="img" aria-label="Illustration of a chrome grab bar mounted diagonally"></div>

  <p class="brand-top">Rail Right</p>
  <p class="brand-bottom">Fitters Inc.</p>
  <p class="tagline">GRAB RAILS, BATH RAILS, &amp; SAFETY RAILS</p>

  <p class="price price--single"><strong>$89.95</strong> Standard Grab Bars</p>
  <p class="price price--double"><strong>$84.95</strong> each for 2</p>
  <p class="price price--triple"><strong>$79.95</strong> each for 3</p>
  <p class="finishes">16 inch Bars available in White, Chrome, &amp; Pewter</p>

  <p class="extras">Also offer Designer Bars &amp;<br>Angle Configurations</p>

  <div class="scene" role="img" aria-label="Illustration of fluffy clouds in a blue sky with a yellow delivery car driving on grass">
    <div class="scene__text">Same Day<br>Delivery<br>AND<br>Installation<br>INCLUDED!</div>
  </div>

  <div class="rooms">
    <div class="rooms__title">Installations Include:</div>
    <div>Any Room</div>
    <div>Bathroom</div>
    <div>Bedroom</div>
    <div>Kitchen</div>
    <div>Stairway</div>
    <div>Garage</div>
    <div>Workshop</div>
    <div>Front and Backdoor</div>
    <div>Bathtub</div>
    <div>Shower Stall</div>
    <div>Toilet Area</div>
    <div>Laundry Room</div>
  </div>
</main>
</body>
</html>
```